quorvel stationary business card and letterhead

THIS PROJECT IS TO DESIGN A BUSINESS CARD DOUBLE SIDES .

Reason: I AM WAITING FOR BEZITH SUBMISION

Industry/Entity Type

Business

Font styles to use
Other font styles liked:
• Chose your font

```html
<!DOCTYPE html>
<html lang="en">
<head>
<meta charset="utf-8">
<title>Quorvel – Business Card</title>
<link rel="stylesheet" href="https://fonts.googleapis.com/css2?family=Questrial&display=swap">
<style>
  :root {
    --backdrop: #d4d4d2;
    --card: #050505;
    --ink-light: #f2f2f2;
    --ink-muted: #cfcfcf;
    --accent: #e2b212;
  }
  * { margin: 0; padding: 0; box-sizing: border-box; }
  html, body {
    width: 1200px;
    height: 1000px;
    overflow: hidden;
    background: var(--backdrop);
    font-family: "Questrial", "Century Gothic", sans-serif;
  }
  .sheet {
    position: relative;
    width: 1200px;
    height: 1000px;
    display: flex;
    flex-direction: column;
    align-items: center;
    justify-content: center;
    gap: 60px;
  }
  .card {
    position: relative;
    width: 580px;
    height: 330px;
    background: var(--card);
    color: var(--ink-light);
    box-shadow: 0 6px 18px rgba(0,0,0,0.18);
  }
  /* Contact side */
  .contact {
    position: absolute;
    top: 46px;
    left: 44px;
  }
  .contact__name {
    font-size: 26px;
    letter-spacing: 0.5px;
    color: var(--ink-light);
    margin-bottom: 6px;
  }
  .contact__credentials {
    font-size: 11px;
    letter-spacing: 0.6px;
    color: var(--ink-muted);
    text-transform: uppercase;
    margin-bottom: 4px;
  }
  .contact__role {
    font-size: 13px;
    letter-spacing: 4px;
    text-transform: uppercase;
    color: var(--ink-light);
    margin-bottom: 4px;
  }
  .contact__line {
    font-size: 10px;
    letter-spacing: 3px;
    color: var(--ink-muted);
    line-height: 1.6;
  }
  /* Brand block */
  .brand {
    display: flex;
    flex-direction: column;
    align-items: flex-start;
  }
  .brand__row {
    display: flex;
    align-items: center;
  }
  .brand__dot {
    border-radius: 50%;
    background: var(--accent);
    flex: none;
  }
  .brand__name {
    color: var(--ink-light);
    line-height: 1;
  }
  .brand__tagline {
    color: var(--accent);
    text-transform: uppercase;
  }
  .brand--small {
    position: absolute;
    right: 34px;
    bottom: 30px;
  }
  .brand--small .brand__dot { width: 30px; height: 30px; margin-right: 8px; }
  .brand--small .brand__name { font-size: 30px; }
  .brand--small .brand__tagline { font-size: 8px; letter-spacing: 2.6px; margin-left: 38px; margin-top: 3px; }
  .brand--large {
    position: absolute;
    top: 50%;
    left: 50%;
    transform: translate(-50%, -50%);
  }
  .brand--large .brand__dot { width: 56px; height: 56px; margin-right: 12px; }
  .brand--large .brand__name { font-size: 56px; }
  .brand--large .brand__tagline { font-size: 11px; letter-spacing: 4.4px; margin-left: 68px; margin-top: 4px; }
</style>
</head>
<body>
  <main class="sheet">
    <section class="card card--contact" aria-label="Card back, contact details">
      <div class="contact">
        <p class="contact__name">Daniel Okwera,</p>
        <p class="contact__credentials">BSc (Food Science), MSc, MBA, CHA</p>
        <p class="contact__role">Consulting Director</p>
        <p class="contact__line">0024 7000 555 018</p>
        <p class="contact__line">www.quorvelconsult.com</p>
      </div>
      <div class="brand brand--small">
        <div class="brand__row">
          <span class="brand__dot"></span>
          <span class="brand__name">Quorvel</span>
        </div>
        <span class="brand__tagline">International Consulting</span>
      </div>
    </section>

    <section class="card card--brand" aria-label="Card front, company name">
      <div class="brand brand--large">
        <div class="brand__row">
          <span class="brand__dot"></span>
          <span class="brand__name">Quorvel</span>
        </div>
        <span class="brand__tagline">International Consulting</span>
      </div>
    </section>
  </main>
</body>
</html>
```